Travel Adventure Challenge Poster/Information Sheet

We have created a corporate incentive travel package we’ve called the “The Quorvex Pursuit Circuit” This is an experiential travel adventure,….not a tour, an adventure designed to awaken the senses, tap into your realm of creativity and resourcefulness, and connect you with a new environment.
“X” for the mystery, as in, “the unknown”
“Challenge” for the competitive element: - each day offers a competitive challenge that calls forth creativity, resourcefulness and team interaction.
“Connection” for the experience of truly relating to the culture that the participant is emerged in.
We require a one-pager (A4) 8.5x11, one-sided informative ad that is directed toward corporate incentive travel clientele and adventure enthusiasts. I've attached 2 logo's One for the event itself and the other for the parent company. (The Quorvex Pursuit Circuit and Bramwell Journey Services) This is a teaser. The goal is to have people contact us by phone, web, or email to find out more information. I've also attached several pages of content and images to choose from...The green, black/grey and white are the standard colors for the logo and we are open to incorporating vibrant complementary colors. Let your creativity flow! We look forward to seeing what you can create!

```html
<!DOCTYPE html>
<html lang="en">
<head>
<meta charset="utf-8">
<title>The Quorvex Pursuit Circuit – Flyer</title>
<link rel="stylesheet" href="https://fonts.googleapis.com/css2?family=Montserrat:wght@600;700&family=PT+Sans:wght@400;700&family=PT+Sans+Narrow:wght@400;700&display=swap">
<style>
  :root{
    --green:#8be20e;
    --green-bright:#97f00f;
    --charcoal:#3f4443;
    --charcoal-deep:#353a39;
    --panel:rgba(70,66,72,.82);
    --ink:#141414;
    --white:#ffffff;
    --page-bg:#e9ebe6;
  }
  html,body{margin:0;padding:0;overflow:hidden;}
  body{width:1200px;height:1000px;background:var(--page-bg);position:relative;font-family:"PT Sans",sans-serif;}
  .flyer{position:absolute;left:195px;top:40px;width:660px;height:855px;overflow:hidden;background:var(--charcoal);box-shadow:0 10px 28px rgba(0,0,0,.35);}
  .hero{position:absolute;left:0;top:0;width:660px;height:605px;}
  .hero-photo{position:absolute;inset:0;background:
      linear-gradient(180deg,#5c6070 0%,#4a5068 30%,#8a6e78 60%,#c98a86 78%,#b8625e 100%);}
  .hero svg.shapes{position:absolute;inset:0;}
  .brand-box{position:absolute;left:0;top:18px;width:271px;height:60px;background:var(--white);display:flex;align-items:center;padding-left:32px;box-sizing:border-box;gap:10px;}
  .brand-box .mark{width:16px;height:16px;background:var(--green);}
  .brand-box .name{font-family:"Montserrat",sans-serif;font-weight:700;font-size:13px;color:var(--charcoal);line-height:1.15;letter-spacing:.3px;}
  .headline{position:absolute;left:20px;top:88px;margin:0;font-family:"Montserrat",sans-serif;font-weight:700;font-size:26px;line-height:27px;color:var(--white);letter-spacing:1.5px;}
  .tagline{position:absolute;left:25px;top:180px;width:200px;margin:0;font-size:12px;line-height:20px;color:var(--ink);text-transform:uppercase;}
  .intro{position:absolute;left:18px;top:222px;width:148px;font-size:13px;line-height:19.5px;color:var(--ink);}
  .intro p{margin:0 0 18px;}
  .thumb{position:absolute;border:3px solid var(--white);box-shadow:4px 5px 8px rgba(0,0,0,.55);}
  .pillars{position:absolute;left:408px;top:186px;width:242px;color:var(--white);font-size:13px;line-height:19.5px;}
  .pillars p{margin:0 0 15px;}
  .pillars b{font-family:"PT Sans Narrow",sans-serif;font-size:18px;font-weight:700;letter-spacing:.3px;}
  .parent-box{position:absolute;left:370px;top:528px;width:290px;height:60px;background:var(--white);padding-left:14px;box-sizing:border-box;display:flex;align-items:center;gap:8px;}
  .parent-box .mark{width:12px;height:12px;background:var(--charcoal);}
  .parent-box .name{font-family:"Montserrat",sans-serif;font-weight:600;font-size:13px;color:var(--charcoal);}
  .promise{position:absolute;left:0;top:605px;width:660px;height:145px;background:var(--charcoal);text-align:center;}
  .promise p{margin:14px 40px 0;font-size:16px;line-height:19px;color:var(--white);}
  .promise h2{margin:12px 40px 0;font-size:20.5px;line-height:26px;font-weight:700;color:var(--green-bright);}
  .dates{position:absolute;left:0;top:750px;width:660px;height:40px;background:var(--green-bright);text-align:center;font-family:"PT Sans Narrow",sans-serif;font-size:30px;line-height:40px;color:var(--white);}
  .contact{position:absolute;left:0;top:790px;width:660px;height:65px;background:var(--charcoal-deep);text-align:center;color:var(--white);font-size:15px;line-height:20px;padding-top:11px;box-sizing:border-box;}
</style>
</head>
<body>
<main class="flyer">
  <section class="hero">
    <div class="hero-photo" role="img" aria-label="Photograph of a businessman in a suit crouched in a sprinter's starting position on a red running track"></div>
    <svg class="shapes" width="660" height="605" viewBox="0 0 660 605" aria-hidden="true">
      <polygon points="0,60 190,60 410,370 140,605 60,605 175,460 0,210" fill="var(--green)"/>
      <polygon points="580,0 660,0 660,605 330,605 405,420" fill="var(--panel)"/>
    </svg>

    <div class="brand-box">
      <span class="mark"></span>
      <span class="name">The Quorvex<br>Pursuit Circuit</span>
    </div>

    <h1 class="headline">COMPETE.<br>CREATE.<br>CONNECT.</h1>
    <p class="tagline">Travel designed to revive and expand creative thinking</p>

    <div class="intro">
      <p>When 1,500 of the top CEO’s from around the world were interviewed, they believed that more than rigor, management, discipline, integrity or even vision, creativity ranked number one.</p>
      <p>The Quorvex Pursuit Circuit has designed a cultural playground for the mind to explore its creative pipeline, incorporating daily challenges that excite, engage, interact and educate.</p>
    </div>

    <div class="thumb" style="left:205px;top:210px;width:94px;height:60px;background:linear-gradient(160deg,#2f5a2a,#6f9a48);" role="img" aria-label="Photo of a hanging bridge in a rainforest canopy"></div>
    <div class="thumb" style="left:265px;top:275px;width:94px;height:66px;background:linear-gradient(170deg,#5f8f3c,#a7c05a);" role="img" aria-label="Photo of a rider on horseback in lush green countryside"></div>
    <div class="thumb" style="left:200px;top:355px;width:99px;height:69px;background:linear-gradient(180deg,#c99a5c,#6a5a44 60%,#5fa9b0);" role="img" aria-label="Photo of a luxury resort pool hall"></div>
    <div class="thumb" style="left:248px;top:440px;width:99px;height:69px;background:linear-gradient(90deg,#4a6a9a,#d86a4a,#e0b850,#4a7ab0);" role="img" aria-label="Photo of women in traditional Vietnamese dresses holding lanterns"></div>
    <div class="thumb" style="left:183px;top:525px;width:102px;height:59px;background:linear-gradient(160deg,#6a5a4a,#b89a78);" role="img" aria-label="Photo of a group cooking class around a table"></div>

    <div class="pillars">
      <p><b>COMPETE.</b> Daily mystery challenges have each participant fully immersed and engaged in a stimulating and educational environment designed to build team skills, leadership and expand creativity while competing daily for prize rewards.</p>
      <p><b>CREATE.</b> Explore cuisine, language, history and communities.</p>
      <p><b>CONNECT.</b> Side by side, with your teammate and the Quorvex crew, you will intimately explore culture, address challenges and build strategies that you can apply to day-to-day living, while having the time of your life!</p>
    </div>

    <div class="parent-box">
      <span class="mark"></span>
      <span class="name">Bramwell Journey Services</span>
    </div>
  </section>

  <section class="promise">
    <p>Your Quorvex team is on the ground beside you ensuring that each element of the event is managed to perfection. We promise that when the daily challenge is complete, luxurious accommodation and relaxation are waiting!</p>
    <h2>Experience a 5* - 10 day mystery challenge immersed in the vibrancy of Vietnam or Costa Rica.</h2>
  </section>

  <div class="dates">Vietnam October 2014 Costa Rica November 2014</div>

  <footer class="contact">
    Contact us to learn more. info@bramwelljourney.cc 1.800.555.0147 x 210<br>
    www.quorvexpursuit.com
  </footer>
</main>
</body>
</html>
```